Webdesign/Updates

We would like a landing page for an online course for our educators. So a website with about 3 to 5 pages - Home, About US, Online course, blog, and Contact us. We have a wordpress site up using a template, but we are looking for something that connects more with our new logo.

Target Market(s)

Educators, workshop trainers/instructors, colleges, community schools, educational institutions, global organizations

Industry/Entity Type

Education

Contact Information for Business Card

Use the words below as place holders for the front:
Name
Title
Address line 1
Address line 2
Email
Phone
Website URL

--the back
Logo
1 short question, use "What do you 1234 about your program?"

Number of Pages Required

4 page

Requirements
Must have
• Home page
• Course Page
• Blog
• right side bar with social media content and invitation to subscribe to newsletter
• see logo colors in document
Nice to have
• Newsletter Page with graphic that can be on this page or page can be sent as a pdf via email or in an email.
Should not have
• Be better than attached description
• clean simple look but stylish

```html
<!DOCTYPE html>
<html lang="en">
<head>
<meta charset="utf-8">
<title>Brightpath Learning – Online Course for our Educators</title>
<link href="https://fonts.googleapis.com/css2?family=Arvo:wght@400;700&family=Mulish:wght@400;600;700&display=swap" rel="stylesheet">
<style>
:root{
  --blue:#29a9e1;
  --blue-deep:#1b8fd0;
  --green:#a6c93a;
  --orange:#f05a28;
  --ink:#1f2328;
  --text:#555a60;
  --muted:#8a8f95;
  --soft:#f7f7f9;
  --line:#d9dde1;
  --footer:#1d1e2c;
  --footer-deep:#15161f;
  --white:#ffffff;
}
*{box-sizing:border-box;margin:0;padding:0}
html,body{width:1200px;height:3789px;overflow:hidden;background:var(--white)}
body{position:relative;font-family:"Mulish",Arial,sans-serif;color:var(--text)}
.abs{position:absolute}
.serif{font-family:"Arvo",Georgia,serif}
.btn{position:absolute;display:flex;align-items:center;justify-content:center;color:var(--white);font-size:13px;font-weight:600;border-radius:2px}
.btn-green{background:var(--green)}
.circle{display:inline-block;width:26px;height:26px;border:2px solid currentColor;border-radius:50%;margin-left:6px;vertical-align:middle}

/* header */
.site-header{left:0;top:0;width:1200px;height:126px}
.brand{left:76px;top:36px;display:flex;align-items:center;gap:12px;font-size:24px;font-weight:600;color:var(--ink)}
.brand-dot{width:40px;height:40px;border-radius:50%;background:var(--green)}
.util-links{right:82px;top:24px;font-size:13px;color:var(--muted);display:flex;gap:22px}
.follow{left:605px;top:64px;font-size:15px;color:var(--ink)}
.search{left:890px;top:60px;width:180px;height:36px;background:#f1f2f3;font-size:13px;color:var(--muted);padding:10px 16px}
.search-btn{left:1070px;top:60px;width:44px;height:36px;background:var(--green)}
.main-nav{left:0;top:126px;width:1200px;height:46px;background:var(--blue);display:flex;padding-left:182px}
.main-nav a{color:var(--white);font-size:14px;font-weight:700;text-decoration:none;height:46px;line-height:46px;padding:0 22px}
.main-nav a.active{background:var(--green)}

/* hero */
.hero{left:0;top:172px;width:1200px;height:480px;background:linear-gradient(90deg,#f3f4f5 0%,#eef0f1 50%,#e8e9e9 100%)}
.hero-photo{left:560px;top:0;width:640px;height:480px;background:linear-gradient(120deg,#e5e4e1,#cfc6bd 60%,#b7aca2)}
.hero-title{left:78px;top:100px;font-size:45px;line-height:56px;color:var(--ink);font-weight:400}
.hero-sub{left:78px;top:220px;font-size:19px;font-weight:600;color:var(--ink)}
.hero-label{left:78px;top:280px;font-size:13px;font-weight:600;color:var(--ink)}
.hero-input{left:78px;top:310px;width:276px;height:42px;background:var(--white);border:1px solid var(--line);font-size:13px;color:var(--muted);padding:12px 16px}
.hero-find{left:361px;top:310px;width:116px;height:42px;background:var(--orange)}

/* overview */
.overview-title{left:131px;top:786px;font-size:31px;color:var(--ink)}
.overview-text{left:131px;top:850px;width:510px;font-size:13px;line-height:26px}
.overview-photo{left:702px;top:796px;width:361px;height:222px;background:linear-gradient(135deg,#c9d3da,#8fa1ae 55%,#5d6e7c)}

/* features */
.features{left:0;top:1132px;width:1200px;height:505px;background:var(--soft);border-top:1px solid #eee;border-bottom:1px solid #eee}
.sec-title{left:0;width:1200px;text-align:center;font-size:31px;color:var(--ink)}
.sec-sub{left:0;width:1200px;text-align:center;font-size:13px;color:var(--muted)}
.feature{top:1340px;width:240px;text-align:center}
.feature svg{display:block;margin:0 auto 30px}
.feature h3{font-size:14px;font-weight:700;color:var(--ink);margin-bottom:10px;letter-spacing:.3px}
.feature p{font-size:12.5px;line-height:19px;text-align:left;padding:0 6px}
.feature .more{display:block;margin-top:22px;font-size:13px;font-weight:700;color:var(--ink)}
.feature .more span{color:var(--orange)}

/* objectives */
.obj{top:1824px;width:320px}
.obj-photo{height:166px}
.obj h3{margin-top:36px;font-size:14px;font-weight:700;color:var(--ink)}
.obj p{margin-top:12px;font-size:13px;line-height:19px;width:260px}
.obj .btn{position:relative;margin-top:26px;width:105px;height:36px}

/* register */
.register{left:0;top:2286px;width:1200px;height:498px;background:linear-gradient(120deg,var(--blue) 0%,var(--blue-deep) 100%)}
.reg-card{left:293px;top:2362px;width:614px;height:356px;background:var(--white)}
.reg-title{left:0;top:40px;width:614px;text-align:center;font-size:31px;color:var(--ink)}
.reg-sub{left:0;top:88px;width:614px;text-align:center;font-size:15px;font-weight:700;color:var(--ink)}
.reg-sub span{color:var(--green)}
.field{height:38px;border:1px solid var(--line);font-size:12px;color:var(--muted);padding:11px 16px}
.reg-submit{left:56px;top:260px;width:480px;height:38px;font-size:15px;font-weight:400}

/* news */
.news{top:3026px;width:300px}
.news h3{font-size:17px;line-height:24px;color:var(--ink);font-weight:400}
.news h3.linked{color:var(--blue);text-decoration:underline}
.news p{margin-top:18px;font-size:12.5px;line-height:18px;width:260px}

/* footer */
.footer{left:0;top:3330px;width:1200px;height:409px;background:var(--footer)}
.footer-bar{left:0;top:3739px;width:1200px;height:50px;background:var(--footer-deep);text-align:center;font-size:12px;line-height:50px;color:var(--muted)}
.foot-brand{left:128px;top:3490px;font-size:22px;font-weight:600;color:var(--white)}
.foot-follow{left:128px;top:3566px;font-size:15px;color:var(--white)}
.foot-col h4{font-size:16px;font-weight:600;color:var(--white);margin-bottom:18px}
.foot-col li{list-style:none;font-size:13px;line-height:22px;color:#c8cad0}
.foot-email{left:841px;top:3511px;width:258px;height:40px;background:var(--white);font-size:13px;font-weight:600;color:var(--ink);padding:11px 22px}
.foot-submit{left:841px;top:3566px;width:112px;height:39px;background:var(--blue-deep);font-weight:400}
</style>
</head>
<body>

<header class="abs site-header">
  <div class="abs brand"><span class="brand-dot"></span>Brightpath Learning</div>
  <nav class="abs util-links"><span>Calendar</span><span>Contacts &amp; Help</span><span>Current Students</span></nav>
  <div class="abs follow">Follow Us : <span class="circle"></span><span class="circle"></span><span class="circle"></span><span class="circle"></span></div>
  <div class="abs search">Search</div>
  <div class="abs search-btn">
    <svg width="44" height="36" viewBox="0 0 44 36"><circle cx="21" cy="17" r="6" fill="none" stroke="#fff" stroke-width="2"/><line x1="25.5" y1="21.5" x2="29" y2="25" stroke="#fff" stroke-width="2"/></svg>
  </div>
</header>

<nav class="abs main-nav">
  <a class="active">HOME</a><a>COURSE</a><a>BLOG</a><a>ABOUT US</a><a>CONTACT US</a><a>GET MORE INFO</a><a>PROGRAMS</a>
</nav>

<section class="abs hero">
  <div class="abs hero-photo" role="img" aria-label="Photo of a smiling educator working on a laptop"></div>
  <h1 class="abs hero-title serif">Online Course for our<br>Educators</h1>
  <p class="abs hero-sub">Advance Your Career. Improve Your Life.</p>
  <p class="abs hero-label">What do You Want To Learn ?</p>
  <div class="abs hero-input">Enter keywords</div>
  <div class="btn hero-find">Find Program</div>
  <svg class="abs" style="left:0;top:400px" width="1200" height="80" viewBox="0 0 1200 80" preserveAspectRatio="none">
    <path d="M0 40 C300 90 700 0 1200 30 L1200 80 L0 80Z" fill="var(--blue)"/>
    <path d="M0 55 C320 100 760 20 1200 48 L1200 80 L0 80Z" fill="#fff"/>
  </svg>
</section>

<h2 class="abs overview-title serif">Online Learning Overview</h2>
<p class="abs overview-text">Visiting Non-Degree (Non-MU) Students seeking to supplement the courses offered by their home institutions or to earn credits during the summer sessions may enroll in MU's online classes. Always consult with your academic advisor at your home institution to ensure that classes taken at Meridian University will be accepted for credit, since the transfer of course and degree credits are determined by the receiving institution.</p>
<div class="btn btn-green" style="left:131px;top:1030px;width:117px;height:42px">Know More</div>
<div class="abs overview-photo" role="img" aria-label="Video still of students learning together at a laptop"></div>

<section class="abs features"></section>
<h2 class="abs sec-title serif" style="top:1214px">The Ultimate Course Design Program Features</h2>
<p class="abs sec-sub" style="top:1268px">Join us for a webinar that helps you to online learning works at Northfield Online Campus.</p>

<div class="abs feature" style="left:102px">
  <svg width="52" height="44" viewBox="0 0 52 44"><rect x="4" y="8" width="44" height="30" fill="none" stroke="var(--blue)" stroke-width="2"/><circle cx="26" cy="20" r="5" fill="none" stroke="var(--orange)" stroke-width="2"/><path d="M17 36 Q26 24 35 36" fill="none" stroke="var(--orange)" stroke-width="2"/></svg>
  <h3>EFFECTIVE LESSIONS</h3>
  <p>Build your expertise. Certificate programs give you the specialization you need to keep ahead of trends. seek.</p>
  <span class="more">Know More <span>›</span></span>
</div>
<div class="abs feature" style="left:360px">
  <svg width="52" height="44" viewBox="0 0 52 44"><rect x="4" y="6" width="44" height="30" fill="none" stroke="var(--blue)" stroke-width="2"/><path d="M22 14 L32 21 L22 28Z" fill="var(--orange)"/><line x1="16" y1="40" x2="36" y2="40" stroke="var(--blue)" stroke-width="2"/></svg>
  <h3>QUALITY VIDEOS</h3>
  <p>Build your expertise. Certificate programs give you the specialization you need to keep ahead of trends. seek.</p>
  <span class="more">Know More <span>›</span></span>
</div>
<div class="abs feature" style="left:620px">
  <svg width="52" height="44" viewBox="0 0 52 44"><rect x="8" y="4" width="36" height="36" fill="none" stroke="var(--blue)" stroke-width="2"/><path d="M16 22 L23 29 L36 14" fill="none" stroke="var(--orange)" stroke-width="2.5"/></svg>
  <h3>AWESOME QUIZZES</h3>
  <p>Build your expertise. Certificate programs give you the specialization you need to keep ahead of trends. seek greater.</p>
  <span class="more">Know More <span>›</span></span>
</div>
<div class="abs feature" style="left:880px">
  <svg width="52" height="44" viewBox="0 0 52 44"><rect x="4" y="6" width="44" height="32" fill="none" stroke="var(--blue)" stroke-width="2"/><line x1="4" y1="14" x2="48" y2="14" stroke="var(--blue)" stroke-width="2"/><line x1="12" y1="22" x2="40" y2="22" stroke="var(--orange)" stroke-width="2"/><line x1="12" y1="29" x2="32" y2="29" stroke="var(--orange)" stroke-width="2"/></svg>
  <h3>HOSTED CONTENT</h3>
  <p>Build your expertise. Certificate programs give you the specialization you need to keep ahead of trends. seek greater.</p>
  <span class="more">Know More <span>›</span></span>
</div>

<h2 class="abs sec-title serif" style="top:1700px">Learning Objective</h2>
<p class="abs sec-sub" style="top:1752px">Join us for a webinar that helps you online learning works at Northfield Online Campus.</p>

<div class="abs obj" style="left:93px">
  <div class="obj-photo" role="img" aria-label="Photo of hands on a laptop showing skill charts" style="background:linear-gradient(135deg,#9a7f6c,#5e5148 60%,#3a3531)"></div>
  <h3>SKILL</h3>
  <p>Current MU students can select from over 100 online classes offered the Fall, Spring and Summer sessions, graduate students.</p>
  <div class="btn btn-green">Know More</div>
</div>
<div class="abs obj" style="left:450px">
  <div class="obj-photo" role="img" aria-label="Photo of a student studying on a laptop at home" style="background:linear-gradient(135deg,#e6e3df,#b9b3ab 60%,#8d8780)"></div>
  <h3>SELF LEARNING</h3>
  <p>Current MU students can select from over 100 online classes offered the Fall, Spring and Summer sessions. graduate students.</p>
  <div class="btn btn-green">Know More</div>
</div>
<div class="abs obj" style="left:798px">
  <div class="obj-photo" role="img" aria-label="Photo of two learners discussing work at a table" style="background:linear-gradient(135deg,#7b6a5c,#a98c70 55%,#4e4038)"></div>
  <h3>KNOWLEDGE</h3>
  <p>Current MU students can select from over 100 online classes offered the Fall, Spring and Summer and graduate students.</p>
  <div class="btn btn-green">Know More</div>
</div>

<section class="abs register" role="img" aria-label="Blue backdrop with a faint photo of a laptop workspace"></section>
<div class="abs reg-card">
  <h2 class="abs reg-title serif">REGISTER NOW</h2>
  <p class="abs reg-sub serif">Trusted by over <span>500+ Students</span></p>
  <div class="abs field" style="left:56px;top:150px;width:236px">Name</div>
  <div class="abs field" style="left:306px;top:150px;width:230px">Email</div>
  <div class="abs field" style="left:56px;top:204px;width:480px">Ph Number *</div>
  <div class="btn btn-green reg-submit">Get it Now</div>
</div>

<h2 class="abs sec-title serif" style="top:2882px">Latesr News</h2>
<p class="abs sec-sub" style="top:2938px">Join us for a webinar that helps you online learning works at Northfield Online Campus.</p>

<article class="abs news" style="left:83px">
  <h3 class="serif">College Ledger ranks Northfield Online Campus as a top provider of online education</h3>
  <p>Northfield Online Campus has once again received the most top-10 rankings of any try for online education. College Ledger...</p>
</article>
<article class="abs news" style="left:472px">
  <h3 class="serif linked">College Ledger ranks Northfield Online Campus as a top provider of online education</h3>
  <p>Northfield Online Campus has once again received the most top-10 rankings of any in thecountry for online education. College...</p>
</article>
<article class="abs news" style="left:844px">
  <h3 class="serif">College Ledger ranks Northfield Online Campus as a top provider of online education</h3>
  <p>Northfield Online Campus has once again received the most top-10 rankings of any institution in thecountry College Ledger .</p>
</article>
<div class="btn btn-green" style="left:528px;top:3231px;width:139px;height:40px">View More</div>

<footer class="abs footer"></footer>
<svg class="abs" style="left:0;top:3300px" width="1200" height="90" viewBox="0 0 1200 90" preserveAspectRatio="none">
  <path d="M0 20 C400 90 800 -10 1200 30 L1200 90 L0 90Z" fill="var(--blue)"/>
  <path d="M0 40 C420 100 820 20 1200 55 L1200 90 L0 90Z" fill="var(--footer)"/>
  <path d="M0 0 L1200 0 L1200 30 C800 -10 400 90 0 20Z" fill="#fff"/>
</svg>
<div class="abs foot-brand">Brightpath Learning</div>
<div class="abs foot-follow">Follow Us : <span class="circle"></span><span class="circle"></span><span class="circle"></span><span class="circle"></span></div>

<div class="abs foot-col" style="left:417px;top:3462px">
  <h4>Quick links</h4>
  <ul><li>Concert Series</li><li>Signature</li><li>Pops</li><li>Matinée</li><li>Baroque &amp; Beyond</li><li>Kinderconcerts</li><li>Family</li><li>Youth Orchestra</li></ul>
</div>
<div class="abs foot-col" style="left:604px;top:3462px">
  <h4>Our address</h4>
  <ul><li>(555) 014-2290</li><li>Harmon Learning Hall</li><li>48 Alder Grove Avenue</li><li>Easton, NY 10099-0000</li></ul>
</div>
<div class="abs foot-col" style="left:841px;top:3462px">
  <h4>Sign Up For Our Newsletter</h4>
</div>
<div class="abs foot-email">Email</div>
<div class="btn foot-submit">Submit</div>

<div class="abs footer-bar">2018 all rights reserved</div>

</body>
</html>
```